Homepage Design for Digital Advertising Company

The website will be very simple, with just one page (the homepage).

We are a new startup company, Quorvane Media, and focus on social media and gaming advertising. We work directly with brands, and with other media agencies. I have attached some details about our company, what we do, and content you can use for the website. I have also attached a screenshot of our logo (high quality files will be provided shortly).

This is an example of a website we really like. They do not do what we do, however their layout is great, and the best part about it is that they really get the message accross of exactly what they do as soon as the page loads. We do not have a product video, so that part does not apply, however i love their basic page layout.
http://www.plindero.com/

We can say something like this:
Simple Social Media and Gaming Advertising (BIG TEXT)
WE DELIVER: Brellows fans and likes, Chirrup followers, Targeted ads and video, and more... (SubText)

On the homepage, we want to have a prominent "Free Consultation" box with a "Submit" button. This box will have input boxes for:
Name
Email
Phone
Or, we can do just a simple email submit as seen here (I like how they did a one long page design BTW)
http://morvexa.com/

Here are some other sites i like:
http://www.talvicor.com/
http://www.gremblo.com/
http://torvanix.net/

Not sure what you will get out of this one, but its too unique to not mention:
http://yuvasi.com/handset/

COLORS:
We are flexible on color scheme. We can change the color of the logo, so dont let that limit your color concepts.

Content on site:
We can use fly out buttons or "more" links for extra text dropdowns if you only want to include an excerpt from each topic in the attached content sheet. Dont want page to be too busy.

Long One Page:
We are not opposed to something like this, by the way
http://morvexa.com/

Target Market(s)

big brands, advertising agencies

Industry/Entity Type

Digital

Requirements
Must have
• Logo
Sign up form
Nice to have
• all the content from our attachment
Should not have
• busy designs, lack of white space, too much text

```html
<!DOCTYPE html>
<html lang="en">
<head>
<meta charset="utf-8">
<title>Quorvane Media — Social Media and Gaming Advertising</title>
<link rel="stylesheet" href="https://fonts.googleapis.com/css2?family=Open+Sans:ital,wght@0,400;0,600;1,600;1,700&family=Arimo:ital,wght@0,400;0,700;1,700&display=swap">
<style>
:root{
  --ink:#222;
  --nav-link:#1f6fb8;
  --header-top:#ffffff;
  --header-bottom:#e9e9e9;
  --rule:#d6d6d6;
  --blue-deep:#0d5a93;
  --blue-mid:#1f7fc2;
  --blue-light:#4aa6df;
  --blue-accent:#2b8fd0;
  --text-body:#6a6a6a;
  --white:#ffffff;
  --footer-top:#7a7a7a;
  --footer-bottom:#5a5a5a;
  --side-dark:#1b2638;
}
*{box-sizing:border-box;margin:0;padding:0}
html,body{width:1200px;height:1084px;overflow:hidden;background:var(--white)}
body{position:relative;font-family:"Arimo",Arial,sans-serif;color:var(--ink)}

/* header */
.site-header{position:absolute;left:0;top:0;width:1200px;height:94px;
  background:linear-gradient(var(--header-top),var(--header-bottom));border-bottom:1px solid var(--rule)}
.brand{position:absolute;left:40px;top:40px;display:flex;align-items:center;gap:10px;
  font-family:"Open Sans",sans-serif;font-weight:400;font-size:31px;color:var(--ink);letter-spacing:-.3px}
.brand-mark{width:14px;height:14px;border-radius:50%;background:var(--blue-mid)}
.main-nav{position:absolute;right:36px;top:0;height:94px;display:flex}
.main-nav a{display:flex;align-items:center;padding:0 28px;font-size:17px;color:var(--nav-link);
  text-decoration:none;border-left:1px solid var(--rule)}
.main-nav a:first-child{border-left:none;color:var(--ink)}

/* hero */
.hero{position:absolute;left:0;top:95px;width:1200px;height:411px;background:var(--side-dark)}
.hero-photo{position:absolute;left:43px;top:0;width:1114px;height:411px;
  background:linear-gradient(160deg,#3f7fc9 0%,#8fb8e0 30%,#2c4f7a 55%,#a9c6e2 75%,#34597f 100%)}
.hero-arrow{position:absolute;top:188px;width:20px;height:34px}
.hero-arrow.prev{left:11px}.hero-arrow.next{right:11px}
.hero-caption{position:absolute;left:444px;top:150px;width:702px;height:142px;border-radius:10px;
  background:rgba(31,112,190,.85);color:var(--white);padding:16px 16px 0 16px}
.hero-title{font-family:"Open Sans",sans-serif;font-style:italic;font-weight:600;font-size:31px;line-height:1.2}
.hero-sub{margin-top:16px;font-family:"Open Sans",sans-serif;font-style:italic;font-weight:600;font-size:17px;line-height:1.2}
.learn-more{position:absolute;right:11px;bottom:11px;width:122px;height:27px;border-radius:8px;
  background:linear-gradient(#5cc6f2,#1e93d3);color:#0a2a45;font-family:"Open Sans",sans-serif;
  font-style:italic;font-weight:600;font-size:14px;display:flex;align-items:center;justify-content:center}

/* services band */
.services{position:absolute;left:0;top:506px;width:1200px;height:134px;
  background:linear-gradient(var(--blue-accent),var(--blue-deep))}
.service{position:absolute;top:0;height:134px}
.service.help{left:0;width:384px;border-right:1px solid #0a3d66}
.service.video{left:384px;width:348px;border-right:1px solid #0a3d66}
.service.display{left:732px;width:468px}
.service-icon{position:absolute;top:28px;width:78px;height:78px;border-radius:8px;background:linear-gradient(135deg,#8fd0f5,#2a78c0)}
.help .service-icon{left:80px}
.video .service-icon{left:42px}
.display .service-icon{left:18px}
.service-text{position:absolute;top:34px;font-family:"Open Sans",sans-serif;font-style:italic;font-weight:600;line-height:1.1;white-space:nowrap}
.help .service-text{left:190px}
.video .service-text{left:156px}
.display .service-text{left:121px}
.service-text .small{display:block;font-size:22px;color:var(--white)}
.service-text .big{display:block;font-size:29px;color:#8fd3f7}
.band-arrow{position:absolute;top:52px;width:16px;height:30px}
.band-arrow.prev{left:16px}.band-arrow.next{right:12px}

/* welcome */
.welcome-photo{position:absolute;left:0;top:640px;width:408px;height:376px;
  background:linear-gradient(#f4f4f4,#dfe3e8)}
.welcome{position:absolute;left:414px;top:656px;width:380px}
.welcome h1{font-family:"Open Sans",sans-serif;font-style:italic;font-weight:600;font-size:23px;color:var(--blue-accent)}
.welcome p{margin-top:14px;font-size:14.2px;line-height:17.3px;color:var(--text-body)}
.welcome p+p{margin-top:17px}

/* consultation form */
.consult{position:absolute;left:815px;top:652px;width:366px;height:354px;border-radius:12px;
  background:radial-gradient(circle at 35% 35%,var(--blue-light),var(--blue-mid) 55%,var(--blue-deep));color:var(--white)}
.consult h2{position:absolute;left:29px;top:16px;font-family:"Open Sans",sans-serif;font-style:italic;font-weight:600;font-size:22px}
.field{position:absolute;left:25px;width:319px;height:40px;display:flex;align-items:center;justify-content:space-between}
.field label{font-size:17px}
.field span{width:248px;height:38px;border-radius:9px;background:linear-gradient(#ffffff,#cfd3d8);
  box-shadow:0 2px 3px rgba(0,0,0,.35)}
.field.name{top:66px}.field.email{top:127px}.field.phone{top:192px}
.call{position:absolute;right:25px;top:253px;font-family:"Open Sans",sans-serif;font-style:italic;font-weight:600;font-size:22px}
.submit{position:absolute;left:97px;top:300px;width:248px;height:38px;border-radius:9px;
  background:linear-gradient(#6f6f6f,#3d3d3d);border:1px solid #2a2a2a;color:var(--white);
  font-family:"Open Sans",sans-serif;font-weight:600;font-size:17px;letter-spacing:.6px;
  display:flex;align-items:center;justify-content:center}

/* footer */
.site-footer{position:absolute;left:0;top:1016px;width:1200px;height:68px;
  background:linear-gradient(var(--footer-top),var(--footer-bottom));color:var(--white)}
.footer-nav{position:absolute;left:23px;top:26px;display:flex;gap:16px}
.footer-nav a,.legal{font-style:italic;font-weight:700;font-size:13px;color:var(--white);text-decoration:none}
.legal{position:absolute;right:27px;top:22px;font-size:12px;word-spacing:1px}
.legal .sep{margin:0 14px}
</style>
</head>
<body>

<header class="site-header">
  <div class="brand"><span class="brand-mark"></span>Quorvane Media</div>
  <nav class="main-nav">
    <a href="#">Home</a><a href="#">Login</a><a href="#">About Us</a><a href="#">FAQ</a>
    <a href="#">Blog</a><a href="#">Testimonials</a><a href="#">Contact Us</a>
  </nav>
</header>

<section class="hero">
  <div class="hero-photo" role="img" aria-label="Glass office towers seen from below against a blue sky with clouds"></div>
  <svg class="hero-arrow prev" viewBox="0 0 20 34"><path d="M16 3 4 17l12 14" fill="none" stroke="#fff" stroke-width="4"/></svg>
  <svg class="hero-arrow next" viewBox="0 0 20 34"><path d="M4 3l12 14L4 31" fill="none" stroke="#fff" stroke-width="4"/></svg>
  <div class="hero-caption">
    <div class="hero-title">Simple Social Media and Gaming Advertising</div>
    <div class="hero-sub">WE DELIVER: Brellows fans and likes, Chirrup followers,<br>Targeted ads and video, and more...</div>
    <div class="learn-more">Learn more</div>
  </div>
</section>

<section class="services">
  <div class="service help">
    <div class="service-icon" role="img" aria-label="Help icon"></div>
    <div class="service-text"><span class="small">How We Can</span><span class="big">Help</span></div>
  </div>
  <div class="service video">
    <div class="service-icon" role="img" aria-label="Video folder icon"></div>
    <div class="service-text"><span class="small">Video</span><span class="big">Distribution</span></div>
  </div>
  <div class="service display">
    <div class="service-icon" role="img" aria-label="Billboard icon"></div>
    <div class="service-text"><span class="small">Display</span><span class="big">Advertisements</span></div>
  </div>
  <svg class="band-arrow prev" viewBox="0 0 16 30"><path d="M13 3 3 15l10 12" fill="none" stroke="#000" stroke-width="3.5"/></svg>
  <svg class="band-arrow next" viewBox="0 0 16 30"><path d="M3 3l10 12L3 27" fill="none" stroke="#000" stroke-width="3.5"/></svg>
</section>

<div class="welcome-photo" role="img" aria-label="Young gamer holding a game controller"></div>

<section class="welcome">
  <h1>Welcome to Quorvane Media</h1>
  <p>As a media buyer, it is extremely important to attract the most targeted audience possible while maximizing your return on investment. We accomplish this by getting your brand in front of your most profitable customers where they spend most of their leisure time, playing games. There are over 100 million people who play games on Brellows everyday for 30 minutes on average.&nbsp; That does not include the casual gamer who plays less often, or gamers on other sites and networks we work with.</p>
  <p>We are able to effectively target any demographic through social gaming from tweens to seniors while they are most focused and engaged. Our platform is capable of attracting your audience using interactive video, display ads, Brellows likes, chirrup follows, and in game sponsorships.</p>
</section>

<aside class="consult">
  <h2>Free Consultation</h2>
  <div class="field name"><label>Name</label><span></span></div>
  <div class="field email"><label>Email</label><span></span></div>
  <div class="field phone"><label>Phone</label><span></span></div>
  <div class="call">Call us - 888-555-0142</div>
  <div class="submit">FIX AN APPOINMENT</div>
</aside>

<footer class="site-footer">
  <nav class="footer-nav">
    <a href="#">Home</a><a href="#">Login</a><a href="#">About Us</a><a href="#">FAQ</a>
    <a href="#">Blog</a><a href="#">Testimonials</a><a href="#">Contact Us</a>
  </nav>
  <div class="legal">© Copyright 2012 Quorvane Media<span class="sep">|</span>Privacy Policy<span class="sep">|</span>Terms of Service</div>
</footer>

</body>
</html>
```